Kestrel Fitness Studio Retail Tube Design

We require a design for cardboard tubes, like images included, which will be the main packaging for the clothing sold in our fitness studio. Kestrel Fitness Studio is an upscale customer service driven fitness studio that is geared towards improving our clients/members quality of life by marrying cutting edge technology like 3D scanning and metabolic measurement with first class training based on 30+ years of experience in the industry.

The project will require a design which revolves around the tube seamlessly including the lid and its top and must include the company logo, which is included, along with our web address (www.kestrelgymhall.example).

The final design should be a bold, sleek design which stands out so when people see the tube they will either know it’s from our studio or be curious as to want company it’s from. Similar to the impact the Moravanti bag has that is given to all their customers.

Target Market(s)

Individuals and groups seeking individualize fitness programs which produce results.

Industry/Entity Type

Clothing

Colors

Designer to choose colors to be used in the design.

Requirements
Must have
• Logo and website address

```html
<!DOCTYPE html>
<html lang="en">
<head>
<meta charset="utf-8">
<title>Kestrel Fitness Studio – Retail Tube Wrap</title>
<link rel="stylesheet" href="https://fonts.googleapis.com/css2?family=Roboto:wght@300&display=swap">
<style>
  :root {
    --wrap-bg: #e5e2df;
    --ink: #2d2b29;
    --brand-red: #a31c2f;
  }
  * { margin: 0; padding: 0; box-sizing: border-box; }
  html, body {
    width: 1200px;
    height: 2913px;
    overflow: hidden;
    background: var(--wrap-bg);
  }
  .tube-wrap {
    position: relative;
    width: 1200px;
    height: 2913px;
    background: var(--wrap-bg);
    font-family: "Roboto", Arial, sans-serif;
    font-weight: 300;
    color: var(--ink);
  }
  .brand-square {
    position: absolute;
    left: 510px;
    top: 880px;
    width: 180px;
    height: 180px;
    background: var(--brand-red);
  }
  .brand-name {
    font-weight: 300;
    font-size: inherit;
    color: var(--ink);
  }
  .brand-name__word {
    position: absolute;
    left: 0;
    width: 1200px;
    top: 1362px;
    text-align: center;
    font-size: 260px;
    line-height: 1;
    letter-spacing: 8px;
    padding-left: 8px;
    white-space: nowrap;
  }
  .brand-name__sub {
    position: absolute;
    left: 0;
    width: 1200px;
    top: 1607px;
    text-align: center;
    font-size: 74px;
    line-height: 1;
    letter-spacing: 14px;
    padding-left: 14px;
    white-space: nowrap;
  }
  .brand-rule {
    position: absolute;
    left: 255px;
    top: 1708px;
    width: 712px;
    height: 2px;
    background: var(--ink);
  }
  .web-address {
    position: absolute;
    left: 0;
    width: 1200px;
    top: 1748px;
    text-align: center;
    font-size: 74px;
    line-height: 1;
    white-space: nowrap;
    color: var(--ink);
  }
</style>
</head>
<body>
  <main class="tube-wrap">
    <div class="brand-square" aria-hidden="true"></div>
    <h1 class="brand-name" aria-label="Kestrel Fitness Studio">
      <span class="brand-name__word">kestrel</span>
      <span class="brand-name__sub">FITNESS STUDIO</span>
    </h1>
    <div class="brand-rule" aria-hidden="true"></div>
    <p class="web-address">www.kestrelgymhall.example</p>
  </main>
</body>
</html>
```